vintage snapframe thank you postcard

I am wanting to use this postcard for my wedding thank you. My theme is: outdoor, rustic, country, vintage, neutral colored. The photo booth at my wedding was in a grain bin on a old victorian couch photos taken with a digital snapframe camera! I want the post card to look like an old fashioned snapframe picture with the border and all. At the bottom saying "thank you" or "Wes and Nadia," "Harwood Wedding", "June 14, 2014," something to that affect. On the back left side leaving room for me to write a personal message thanking them for the help/gift/support. The back right side left for the name and address. I will add a wedding picture of the two of us to the front (from our wedding day). Anything that gives the post card a vintage old time feeling is great!! I have a general idea of what I want but, now I know you guys can take care of the rest for me! :) thank you in advance!! -Nadia

Target Market(s)

family, friends - all ages!

Industry/Entity Type

Wedding

Requirements
Must have
• "snapframe photo" look
vintage
"Thank you"
"Wes and Nadia"
Nice to have
• June 14, 2014

```html
<!DOCTYPE html>
<html lang="en">
<head>
<meta charset="utf-8">
<title>Harwood Wedding – Thank You</title>
<link href="https://fonts.googleapis.com/css2?family=Pinyon+Script&family=Cutive&family=Indie+Flower&display=swap" rel="stylesheet">
<style>
  :root {
    --wood-light: #93d9c0;
    --wood-mid: #74c4a8;
    --wood-dark: #4f9c84;
    --wood-seam: rgba(35,70,60,0.45);
    --ink-brown: #6b3a20;
    --paper: #f6f1e4;
    --paper-shade: #e6dcc6;
    --photo-light: #f4ecdd;
    --photo-mid: #dccfc2;
    --photo-edge: #8d7fa3;
    --caption: #5a5650;
    --white: #ffffff;
  }
  * { margin: 0; padding: 0; box-sizing: border-box; }
  html, body { width: 931px; height: 1200px; overflow: hidden; background: #ddd; }
  .card {
    position: relative;
    width: 931px;
    height: 1200px;
    overflow: hidden;
  }
  .card__backdrop {
    position: absolute; inset: 0;
    background:
      repeating-linear-gradient(180deg, transparent 0 118px, var(--wood-seam) 118px 121px, rgba(255,255,255,0.18) 121px 123px),
      repeating-linear-gradient(180deg, rgba(255,255,255,0.06) 0 9px, rgba(0,0,0,0.03) 9px 17px, transparent 17px 31px),
      linear-gradient(90deg, rgba(40,80,70,0.22), transparent 22%, transparent 78%, rgba(40,80,70,0.22)),
      linear-gradient(180deg, var(--wood-mid) 0%, var(--wood-light) 30%, var(--wood-mid) 60%, var(--wood-dark) 100%);
  }
  .card__band {
    position: absolute; left: 0; right: 0;
    background: rgba(255,255,255,0.08);
    border-top: 3px solid var(--wood-seam);
    border-bottom: 3px solid var(--wood-seam);
  }
  .card__band--top { top: 180px; height: 118px; }
  .card__band--bottom { top: 1030px; height: 170px; border-bottom: none; background: rgba(0,0,0,0.06); }
  .title {
    position: absolute;
    left: 58px; top: 6px;
    font-family: "Pinyon Script", cursive;
    font-weight: 400;
    font-size: 164px;
    line-height: 1.2;
    color: var(--ink-brown);
    text-shadow: 2px 2px 0 rgba(255,255,255,0.7), -1px -1px 0 rgba(255,255,255,0.5);
    white-space: nowrap;
  }
  .event {
    position: absolute;
    right: 50px; top: 196px;
    font-family: "Cutive", serif;
    color: var(--white);
    font-size: 23px;
    letter-spacing: 5px;
    line-height: 38px;
    text-align: center;
    text-shadow: 1px 1px 2px rgba(0,0,0,0.35);
  }
  .snapframe {
    position: absolute;
    background: var(--paper);
    box-shadow: 3px 5px 12px rgba(0,0,0,0.35), inset 0 0 30px var(--paper-shade);
  }
  .snapframe__photo {
    position: absolute;
    background: radial-gradient(ellipse at 50% 45%, var(--photo-light) 0%, var(--photo-mid) 70%, var(--photo-edge) 100%);
    box-shadow: inset 0 0 18px rgba(80,60,100,0.45);
  }
  .snapframe__caption {
    position: absolute;
    font-family: "Indie Flower", cursive;
    color: var(--caption);
    white-space: nowrap;
  }
  .snapframe--main { left: 51px; top: 354px; width: 594px; height: 524px; transform: rotate(-0.6deg); }
  .snapframe--main .snapframe__photo { left: 30px; top: 30px; width: 534px; height: 402px; }
  .snapframe--main .snapframe__caption { left: 36px; top: 446px; font-size: 36px; }
  .snapframe--small-a { left: 504px; top: 786px; width: 180px; height: 234px; transform: rotate(-3deg); }
  .snapframe--small-b { left: 692px; top: 774px; width: 196px; height: 240px; transform: rotate(3deg); }
  .snapframe--small-a .snapframe__photo,
  .snapframe--small-b .snapframe__photo { left: 14px; top: 16px; right: 14px; height: 168px; }
  .snapframe--small-a .snapframe__caption,
  .snapframe--small-b .snapframe__caption { right: 16px; bottom: 8px; font-size: 19px; }
  .message {
    position: absolute;
    left: 0; right: 0; top: 1046px;
    text-align: center;
    font-family: "Indie Flower", cursive;
    color: var(--white);
    font-size: 20px;
    line-height: 37px;
    white-space: nowrap;
    text-shadow: 1px 1px 3px rgba(0,0,0,0.6);
  }
</style>
</head>
<body>
<main class="card">
  <div class="card__backdrop" role="img" aria-label="Weathered teal painted wooden boards with chipped paint"></div>
  <div class="card__band card__band--top"></div>
  <div class="card__band card__band--bottom"></div>

  <h1 class="title">Thank You</h1>
  <p class="event">HARWOOD WEDDING<br>JUNE 14, 2014</p>

  <figure class="snapframe snapframe--main">
    <div class="snapframe__photo" role="img" aria-label="Wedding day photo of the couple"></div>
    <figcaption class="snapframe__caption">Wes and Nadia Harwood</figcaption>
  </figure>

  <figure class="snapframe snapframe--small-a">
    <div class="snapframe__photo" role="img" aria-label="Wedding party photo"></div>
    <figcaption class="snapframe__caption">Wedding Party</figcaption>
  </figure>

  <figure class="snapframe snapframe--small-b">
    <div class="snapframe__photo" role="img" aria-label="Wedding party photo"></div>
    <figcaption class="snapframe__caption">Wedding Party</figcaption>
  </figure>

  <p class="message">
    A loving note can barely express how you added to our happiness on this magical day.<br>
    We would like to send our sincerest thanks for your thoughts, your gifts and your presence in our lives!<br>
    ♡ love Wes &amp; Nadia ♡
  </p>
</main>
</body>
</html>
```